Bref créative
Brisk Lattice Cards & Stationary
Project #2
Corporate
Carl Wendimeer
VP of Business Development
2841 Thornbury Lane
Marlow Falls, MN 55612
cwendimeer@brisklattice-mail.com
www.brisklattice-mail.com
Here is our logo

```html
<!DOCTYPE html>
<html lang="en">
<head>
<meta charset="utf-8">
<title>Brisk Lattice — Cards &amp; Stationery</title>
<link rel="stylesheet" href="https://fonts.googleapis.com/css2?family=Open+Sans:wght@400;600;700&display=swap">
<style>
:root{
  --bg:#e4e5e7;
  --paper:#ffffff;
  --navy:#1b3f7a;
  --blue:#2a6bb5;
  --sky:#3f8fd6;
  --grey:#9aa0a7;
  --grey-card:#b9bdc2;
  --ink:#4a4f57;
  --shadow:0 3px 8px rgba(0,0,0,.22);
}
*{margin:0;padding:0;box-sizing:border-box}
html,body{width:1200px;height:686px;overflow:hidden;background:var(--bg);font-family:"Open Sans",Arial,sans-serif;color:var(--ink)}
.canvas{position:relative;width:1200px;height:686px}
.piece{position:absolute;background:var(--paper);box-shadow:var(--shadow);overflow:hidden}
.brand{display:flex;align-items:center;gap:6px;font-weight:700;color:var(--blue);white-space:nowrap;line-height:1}
.brand .mark{display:block;background:var(--blue);flex:none}
.brand.on-dark{color:#fff}
.brand.on-dark .mark{background:#fff}
.tiny{font-size:5px;line-height:1.5;color:var(--ink)}
.rule{position:absolute;left:0;right:0;bottom:0;height:3px;background:linear-gradient(90deg,var(--navy),var(--sky))}

/* notepad sheet */
.note-sheet{left:130px;top:12px;width:345px;height:176px}
.note-sheet .brand{position:absolute;left:16px;top:18px;font-size:13px}
.note-sheet .brand .mark{width:12px;height:12px}

/* top row cards */
.card-sm{height:64px}
.card-blue{background:linear-gradient(135deg,var(--navy),var(--blue))}
.card-grey{background:linear-gradient(135deg,#c9ccd0,var(--grey))}
.card-a{left:512px;top:100px;width:126px}
.card-b{left:655px;top:100px;width:170px}
.card-c{left:838px;top:96px;width:124px;height:68px}
.card-d{left:980px;top:96px;width:132px;height:68px}
.card-sm .brand{font-size:9px}
.card-sm .brand .mark{width:8px;height:8px}
.card-a .brand{position:absolute;left:10px;top:26px}
.card-c .brand,.card-d .brand{position:absolute;left:50%;top:50%;transform:translate(-50%,-50%)}
.card-b .brand{position:absolute;left:10px;top:12px;font-size:7px}
.card-b .brand .mark{width:6px;height:6px}
.card-b .who{position:absolute;right:10px;top:14px;text-align:right}
.card-b .who strong{display:block;font-size:6px;color:var(--navy)}
.card-b .contact{position:absolute;left:10px;bottom:10px}

/* envelope with flap */
.envelope-open{left:25px;top:200px;width:225px;height:188px;background:transparent;box-shadow:none;overflow:visible}
.envelope-open svg{display:block;filter:drop-shadow(0 3px 5px rgba(0,0,0,.2))}
.envelope-open .brand{position:absolute;left:50%;transform:translateX(-50%);font-size:8px}
.envelope-open .brand .mark{width:7px;height:7px}
.envelope-open .flap-brand{top:24px}
.envelope-open .body-brand{top:118px}

/* letterheads */
.letterhead{top:195px;width:305px;height:443px}
.letter-1{left:268px}
.letter-2{left:592px}
.letterhead .brand{position:absolute;left:16px;top:20px;font-size:15px}
.letterhead .brand .mark{width:13px;height:13px}
.letterhead .head-contact{position:absolute;right:16px;top:18px;text-align:right}
.letterhead .foot-contact{position:absolute;right:16px;bottom:10px;text-align:right}
.letterhead .rule{height:4px}

/* small white card */
.card-e{left:988px;top:262px;width:104px;height:68px}
.card-e .brand{position:absolute;left:50%;top:50%;transform:translate(-50%,-50%);font-size:8px}
.card-e .brand .mark{width:7px;height:7px}

/* business envelope */
.envelope-long{left:812px;top:362px;width:343px;height:150px}
.envelope-long .brand{position:absolute;left:16px;top:18px;font-size:13px}
.envelope-long .brand .mark{width:11px;height:11px}
.envelope-long .return{position:absolute;left:16px;top:40px}

/* bottom-left cards */
.card-f{left:105px;top:438px;width:133px;height:64px}
.card-f .brand{position:absolute;left:10px;top:12px;font-size:8px}
.card-f .brand .mark{width:7px;height:7px}
.card-f .who{position:absolute;right:10px;top:30px;text-align:right}
.card-f .who strong{display:block;font-size:5.5px;color:var(--navy)}
.card-g{left:105px;top:520px;width:133px;height:80px}
.card-g .brand{position:absolute;left:50%;top:50%;transform:translate(-50%,-50%);font-size:9px}
.card-g .brand .mark{width:8px;height:8px}

/* featured business card */
.card-front{left:920px;top:530px;width:235px;height:145px}
.card-front .brand{position:absolute;left:16px;top:20px;font-size:14px}
.card-front .brand .mark{width:12px;height:12px}
.card-front .who{position:absolute;right:16px;top:62px;text-align:right}
.card-front .who strong{display:block;font-size:10px;color:var(--navy);font-weight:600}
.card-front .who span{font-size:6px}
.card-front .contact{position:absolute;left:16px;top:72px;font-size:6px}
.card-front .rule{height:4px}
</style>
</head>
<body>
<main class="canvas">

  <section class="piece note-sheet">
    <div class="brand"><span class="mark"></span>Brisk Lattice</div>
  </section>

  <section class="piece card-sm card-blue card-a">
    <div class="brand on-dark"><span class="mark"></span>Brisk Lattice</div>
  </section>

  <section class="piece card-sm card-b">
    <div class="brand"><span class="mark"></span>Brisk Lattice</div>
    <div class="who tiny"><strong>Carl Wendimeer</strong>VP of Business Development</div>
    <div class="contact tiny">cwendimeer@brisklattice-mail.com<br>www.brisklattice-mail.com</div>
  </section>

  <section class="piece card-sm card-blue card-c">
    <div class="brand on-dark"><span class="mark"></span>Brisk Lattice</div>
  </section>

  <section class="piece card-sm card-grey card-d">
    <div class="brand on-dark"><span class="mark"></span>Brisk Lattice</div>
  </section>

  <section class="piece envelope-open">
    <svg width="225" height="188" viewBox="0 0 225 188">
      <defs>
        <linearGradient id="flapFill" x1="0" y1="0" x2="1" y2="1">
          <stop offset="0" stop-color="#1b3f7a"/>
          <stop offset="1" stop-color="#2a6bb5"/>
        </linearGradient>
      </defs>
      <rect x="0" y="0" width="225" height="80" fill="url(#flapFill)"/>
      <rect x="0" y="80" width="225" height="108" fill="#ffffff"/>
      <path d="M0 80 L112 130 L225 80" fill="none" stroke="#d5d8dc" stroke-width="1"/>
    </svg>
    <div class="brand on-dark flap-brand"><span class="mark"></span>Brisk Lattice</div>
    <div class="brand body-brand"><span class="mark"></span>Brisk Lattice</div>
  </section>

  <section class="piece letterhead letter-1">
    <div class="brand"><span class="mark"></span>Brisk Lattice</div>
    <div class="head-contact tiny">2841 Thornbury Lane, Marlow Falls, MN 55612<br>Tel 952 555 0142<br>www.brisklattice-mail.com</div>
    <div class="rule"></div>
  </section>

  <section class="piece letterhead letter-2">
    <div class="brand"><span class="mark"></span>Brisk Lattice</div>
    <div class="foot-contact tiny">2841 Thornbury Lane, Marlow Falls, MN 55612 · www.brisklattice-mail.com</div>
    <div class="rule"></div>
  </section>

  <section class="piece card-e">
    <div class="brand"><span class="mark"></span>Brisk Lattice</div>
  </section>

  <section class="piece envelope-long">
    <div class="brand"><span class="mark"></span>Brisk Lattice</div>
    <div class="return tiny">2841 Thornbury Lane<br>Marlow Falls, MN 55612</div>
    <div class="rule"></div>
  </section>

  <section class="piece card-f">
    <div class="brand"><span class="mark"></span>Brisk Lattice</div>
    <div class="who tiny"><strong>Carl Wendimeer</strong>VP of Business Development</div>
  </section>

  <section class="piece card-grey card-g">
    <div class="brand on-dark"><span class="mark"></span>Brisk Lattice</div>
  </section>

  <section class="piece card-front">
    <div class="brand"><span class="mark"></span>Brisk Lattice</div>
    <div class="contact tiny">2841 Thornbury Lane<br>Marlow Falls, MN 55612<br>Cell 952 555 0187<br>cwendimeer@brisklattice-mail.com<br>www.brisklattice-mail.com</div>
    <div class="who"><strong>Carl Wendimeer</strong><span>VP of Business Development</span></div>
    <div class="rule"></div>
  </section>

</main>
</body>
</html>
```